Business Card Design and Basic Text Logo

We are looking for a business card design for an e-business company. Our business is the parent company of a few website businesses. The final logo and business card design will communicate a conservative but modern and expansive business

The Logo text is: 57Commerce
We would also like a basic text logo design for 57Commerce. The logo could also fill up the reverse side of the business card.

The colours we would like to use are:
White
Navy
Black

This is the text that will be added to the card:

Dean Calloway
Business Development Manager

Phone: +61 417 586 924
Email: dean.calloway@57commerce.com.au

Industry/Entity Type

Business

Logo Text

57Commerce

Logo styles of interest
Pictorial/Combination Logo
Requirements
Must have
• Modern and attractive design
Nice to have
• communicate a conservative but modern and expansive business
Should not have
• Should be too dull and plan
• But also should be overly colourful

```html
<!DOCTYPE html>
<html lang="en">
<head>
<meta charset="utf-8">
<title>57Commerce — Business Card</title>
<link rel="stylesheet" href="https://fonts.googleapis.com/css2?family=Quicksand:wght@300;400;500&display=swap">
<style>
  :root {
    --card-center: #2c3134;
    --card-edge: #0b0c0d;
    --ink-white: #ffffff;
    --ink-soft: #e9eef0;
    --ghost-number: rgba(255, 255, 255, 0.045);
    --accent-blue: #4cc3f5;
    --font-main: 'Quicksand', sans-serif;
  }
  html, body {
    margin: 0;
    padding: 0;
    width: 1200px;
    height: 704px;
    overflow: hidden;
    background: var(--card-edge);
  }
  .card {
    position: relative;
    width: 1200px;
    height: 704px;
    overflow: hidden;
    font-family: var(--font-main);
    background: radial-gradient(ellipse 620px 480px at 730px 330px, var(--card-center) 0%, #1a1d1f 55%, var(--card-edge) 100%);
  }
  .ghost-number {
    position: absolute;
    left: 48px;
    top: 46px;
    margin: 0;
    font-size: 310px;
    line-height: 1;
    font-weight: 500;
    color: var(--ghost-number);
    letter-spacing: -6px;
  }
  .brand {
    position: absolute;
    left: 700px;
    top: 118px;
    display: flex;
    align-items: center;
    gap: 22px;
  }
  .brand-square {
    width: 34px;
    height: 34px;
    background: var(--accent-blue);
  }
  .brand-name {
    margin: 0;
    font-size: 64px;
    line-height: 1;
    font-weight: 400;
    color: var(--ink-white);
  }
  .identity {
    position: absolute;
    right: 618px;
    top: 310px;
    text-align: right;
    color: var(--ink-white);
  }
  .identity-name {
    margin: 0;
    font-size: 48px;
    line-height: 1.1;
    font-weight: 400;
  }
  .identity-role {
    margin: 6px 0 0;
    font-size: 26px;
    line-height: 1.1;
    font-weight: 400;
    color: var(--ink-soft);
  }
  .ornament {
    position: absolute;
    width: 33px;
    background: linear-gradient(180deg, var(--accent-blue), #3aa9dc);
  }
  .ornament-identity { left: 609px; top: 303px; height: 102px; }
  .ornament-contact  { left: 419px; top: 491px; height: 102px; }
  .contact {
    position: absolute;
    left: 469px;
    top: 505px;
    margin: 0;
    padding: 0;
    list-style: none;
    color: var(--ink-white);
    font-size: 29px;
    font-weight: 400;
    line-height: 39px;
  }
</style>
</head>
<body>
  <main class="card">
    <p class="ghost-number" aria-hidden="true">57</p>

    <header class="brand">
      <div class="brand-square" aria-hidden="true"></div>
      <h1 class="brand-name">57Commerce</h1>
    </header>

    <section class="identity">
      <h2 class="identity-name">Dean Calloway</h2>
      <p class="identity-role">Business Development Manager</p>
    </section>
    <div class="ornament ornament-identity" role="img" aria-label="Stacked blue diamond ornament"></div>

    <div class="ornament ornament-contact" role="img" aria-label="Stacked blue diamond ornament"></div>
    <ul class="contact">
      <li class="contact-phone">Phone: +61 417 586 924</li>
      <li class="contact-email">Email: dean.calloway@57commerce.com.au</li>
    </ul>
  </main>
</body>
</html>
```